Interior designer needs a gorgeous, chic business card design.

A new, small Interior Design firm needs a business card that is chic, contemporary and elegant. Nothing over the top. My interiors are contemporary classic with an elegant feel to them. I like to use quality finishes and products rather than follow the latest fads. Projects can be anything from Pre start selections, bathrooms, kitchens, bedrooms, custom upholstery, furniture, rugs and art etc. The final design should display quality and an achievable sense of chic. I am open to all colours including black but not limited to this.

```html
<!DOCTYPE html>
<html lang="en">
<head>
<meta charset="utf-8">
<title>Vela Interiors – Business Card</title>
<link rel="stylesheet" href="https://fonts.googleapis.com/css2?family=Gilda+Display&family=Federo&display=swap">
<style>
  :root {
    --page: #ffffff;
    --card-black: #0b0b0b;
    --panel-dark: #161616;
    --panel-mid: #262626;
    --gold: #c9a23a;
    --gold-light: #e6c76a;
    --silver: #c8c8c8;
    --text-light: #d9d9d9;
    --text-dim: #a8a8a8;
    --ghost: rgba(255, 255, 255, 0.05);
  }
  * { box-sizing: border-box; margin: 0; padding: 0; }
  html, body {
    width: 1200px;
    height: 900px;
    overflow: hidden;
    background: var(--page);
  }
  .canvas {
    position: relative;
    width: 1200px;
    height: 900px;
  }
  .card {
    position: absolute;
    top: 300px;
    width: 520px;
    height: 300px;
    border-radius: 26px;
    background: var(--card-black);
    box-shadow: 0 18px 30px rgba(0, 0, 0, 0.18);
    overflow: hidden;
  }
  .card--front { left: 50px; }
  .card--back { left: 630px; }

  /* Front */
  .gold-frame {
    position: absolute;
    inset: 12px;
    border: 6px solid var(--gold);
    border-radius: 18px;
    background: linear-gradient(90deg, var(--gold), var(--gold-light), var(--gold)) border-box;
  }
  .damask-field {
    position: absolute;
    inset: 18px;
    border-radius: 13px;
    background: radial-gradient(ellipse at center, var(--panel-mid) 0%, var(--panel-dark) 55%, var(--card-black) 100%);
  }
  .brand {
    position: absolute;
    inset: 0;
    display: flex;
    flex-direction: column;
    align-items: center;
    justify-content: center;
    font-family: "Gilda Display", serif;
    color: var(--silver);
    font-weight: 400;
  }
  .brand__name {
    font-size: 58px;
    letter-spacing: 4px;
    line-height: 1;
  }
  .brand__sub {
    font-size: 20px;
    letter-spacing: 6px;
    margin-top: 4px;
  }

  /* Back */
  .ghost-name {
    position: absolute;
    inset: 0;
    display: flex;
    align-items: center;
    justify-content: center;
    font-family: "Gilda Display", serif;
    font-size: 84px;
    letter-spacing: 6px;
    color: var(--ghost);
  }
  .contact {
    position: absolute;
    inset: 0;
    padding-top: 78px;
    text-align: center;
    font-family: "Gilda Display", serif;
  }
  .contact__name {
    color: var(--gold);
    font-size: 20px;
    letter-spacing: 0.5px;
  }
  .contact__qual,
  .contact__role {
    color: var(--text-dim);
    font-size: 12px;
    margin-top: 3px;
  }
  .contact__lines {
    margin-top: 30px;
    font-family: "Federo", sans-serif;
    color: var(--text-light);
    font-size: 18px;
    line-height: 1.45;
  }
  .contact__lines span { display: block; }
</style>
</head>
<body>
  <main class="canvas">
    <section class="card card--front">
      <div class="gold-frame"></div>
      <div class="damask-field" role="img" aria-label="Black tonal damask pattern background"></div>
      <div class="brand">
        <span class="brand__name">VELA</span>
        <span class="brand__sub">Interiors</span>
      </div>
    </section>

    <section class="card card--back">
      <div class="ghost-name" aria-hidden="true">VELA</div>
      <div class="contact">
        <p class="contact__name">Mara Lune Hadley</p>
        <p class="contact__qual">(Dip. Interior Design)</p>
        <p class="contact__role">Director</p>
        <p class="contact__lines">
          <span>0412555018</span>
          <span>mara@velainteriors.com.au</span>
          <span>www.velainteriors.com</span>
        </p>
      </div>
    </section>
  </main>
</body>
</html>
```